Creation of a Velunta website

Velunta is a company% 26 # 233; t% 26 # 233; consulting that accompanies Swiss companies or% 26 # 233; strang% 26 # 232; res in the d% 26 # 233; development of their business on the market% 26 # 233; Switzerland by providing strategic contacts (personalized contact program% 26 # 233; s) or market information% 26 # 233; (% 26 # 233; market research% 26 # 233;) and by providing administrative support (repr% 26 # 233; tax representation) or logistics (organization of% 26 # 233; v% 26 # 233; nement, assistance for participation% 26 # 224; fairs). Our customers are mainly European companies wishing to develop their business in Switzerland. N% 26 # 233; however, our services are% 26 # 233; also aimed at Swiss companies wishing to develop in other parts of Switzerland. Our site must therefore be% 26 # 234; capable of being translated into several languages. The services offered% 26 # 233; s by Velunta may also% 26 # 233; also% 26 # 39;% 26 # 233; tender% 26 # 224; promoting tourism in Switzerland for countries or regions% 26 # 233; foreigners or% 26 # 224; the promotion of trade fairs or fairs with% 26 # 232; sd% 26 # 39; companies of the sectors concerned% 26 # 233; s. It is therefore n% 26 # 233; necessary to be able to add sub-headings of services which can% 26 # 234; be displayed% 26 # 233; es or hide% 26 # 233; es as required. We are 2 associates% 26 # 233; s, low% 26 # 233; s in the French-speaking parts (Neuch% 26 # 226; tel) and al% 26 # 233; manique (Zurich) of Switzerland.

Target Market(s)

Swiss or European companies wishing to develop their activities in Switzerland.

Coding

Coded - Design and coding required

Colors

Designer to choose colors to be used in the design.

Requirements
Must have
• A home page A section of% 26 # 233; writing the services offered% 26 # 233; es by Velunta with the possibility% 26 # 233; d% 26 # 39; add sub-headings which can% 26 # 234; be displayed% 26 # 233; e or hidden% 26 # 233; e A page with the r% 26 # 233; f% 26 # 233; which can be displayed% 26 # 233; e or hidden% 26 # 233; e A page of% 26 # 233; writing l% 26 # 39;% 26 # 233; team A page with form contact, addresses and int card% 26 # 233; gr% 26 # 233; e The site must% 26 # 234; be low% 26 # 233; on a CMS allowing% 26 # 39;% 26 # 234; to be autonomous in modifying the website The possibility% 26 # 233; to be able to translate the site into several languages (FR, EN, DE, IT, NL, ...)

```html
<!DOCTYPE html>
<html lang="en">
<head>
<meta charset="utf-8">
<title>Velunta – Business Development</title>
<link rel="stylesheet" href="https://fonts.googleapis.com/css2?family=Rajdhani:wght@500;600;700&family=Roboto:wght@400;500;700&display=swap">
<style>
:root{
  --navy:#1c3650;
  --navy-band:#2b4a66;
  --ink:#222b33;
  --muted:#5d6670;
  --line:#cfd5db;
  --paper:#ffffff;
  --mist:#f2f4f7;
  --hero-a:#2e3d4d;
  --hero-b:#6f7d8b;
}
*{box-sizing:border-box;margin:0;padding:0}
html,body{width:1200px;height:4680px;overflow:hidden}
body{position:relative;background:var(--paper);font-family:"Roboto",Arial,sans-serif;color:var(--ink)}
.abs{position:absolute}
.heading{font-family:"Rajdhani",Arial,sans-serif;font-weight:700;color:var(--ink);letter-spacing:.5px}
.rule{position:absolute;height:3px;width:64px;background:var(--navy)}
.btn{position:absolute;display:flex;align-items:center;justify-content:center;font-family:"Rajdhani",Arial,sans-serif;font-weight:700;font-size:16px;letter-spacing:.5px;border-radius:3px}
.btn-dark{background:var(--navy);color:#fff}
.btn-light{background:#fff;color:var(--navy)}
.photo{position:absolute}

/* hero */
.hero{left:0;top:0;width:1200px;height:745px;background:linear-gradient(160deg,#4a5866 0%,var(--hero-a) 45%,#1f2a36 100%)}
.hero .photo{inset:0;background:radial-gradient(ellipse at 55% 30%,var(--hero-b) 0%,transparent 60%)}
.brand{left:143px;top:48px;display:flex;align-items:center;gap:16px}
.brand-mark{width:48px;height:48px;border-radius:10px;background:#fff}
.brand-name{font-family:"Rajdhani",Arial,sans-serif;font-weight:500;font-size:40px;letter-spacing:4px;color:#fff}
.nav{left:552px;top:62px;display:flex;gap:26px;font-family:"Rajdhani",Arial,sans-serif;font-weight:600;font-size:15px;color:#fff;letter-spacing:.5px}
.nav .active{text-decoration:underline;text-underline-offset:4px}
.lang{left:998px;top:57px;width:56px;height:30px;border:1px solid rgba(255,255,255,.7);border-radius:6px;color:#fff;font-family:"Rajdhani",Arial,sans-serif;font-weight:600;font-size:14px;display:flex;align-items:center;justify-content:center;gap:4px}
.hero-title{left:0;width:1200px;top:368px;text-align:center;font-family:"Rajdhani",Arial,sans-serif;font-weight:700;font-size:56px;color:#fff;letter-spacing:2px}
.hero-sub{left:0;width:1200px;top:436px;text-align:center;font-family:"Rajdhani",Arial,sans-serif;font-weight:500;font-size:23px;color:#fff}
.slide-arrow{top:362px;width:30px;height:30px;border-radius:50%;background:#fff;display:flex;align-items:center;justify-content:center}
.dots{left:574px;top:673px;display:flex;gap:10px;align-items:center}
.dots span{width:11px;height:11px;border-radius:50%;background:#fff;opacity:.85}
.dots span:first-child{width:16px;height:16px;opacity:1}

/* welcome */
.welcome-title{left:143px;top:850px;font-size:38px}
.welcome-text{left:143px;top:945px;width:430px;font-size:14.5px;line-height:25.6px;color:var(--muted)}
.welcome-photo{left:655px;top:844px;width:400px;height:402px;border-radius:90px;background:linear-gradient(135deg,#d7dbe0,#8f99a4 55%,#4b5866)}

/* services */
.services-band{left:0;top:1364px;width:1200px;height:240px;background:var(--navy-band)}
.services-title{left:0;width:1200px;top:1446px;text-align:center;font-size:38px;color:#fff}
.service-card{top:1600px;width:392px;height:518px;overflow:hidden}
.service-card .photo{inset:0}
.service-card .shade{position:absolute;inset:0;background:linear-gradient(180deg,rgba(20,30,42,0) 40%,rgba(20,30,42,.85) 100%)}
.service-name{position:absolute;left:44px;font-family:"Rajdhani",Arial,sans-serif;font-weight:700;font-size:16px;color:#fff;letter-spacing:.5px;line-height:24px}
.service-text{position:absolute;left:44px;width:250px;font-size:13.5px;line-height:22px;color:#e4e8ec}
.service-go{position:absolute;left:44px}
.service-icon{position:absolute;left:44px;width:60px;height:60px;border-radius:12px;border:2px solid #fff}

/* testimonials */
.test-title{left:0;width:1200px;top:2212px;text-align:center;font-size:38px}
.test-photo{left:216px;top:2333px;width:240px;height:240px;border-radius:60px;background:linear-gradient(135deg,#a56b4c,#c9b7a5 50%,#4f5f70)}
.quote-mark{font-family:Georgia,serif;font-size:64px;font-weight:700;color:var(--ink);line-height:1}
.test-text{left:495px;top:2366px;width:475px;font-size:14.5px;line-height:25.6px;color:var(--muted);text-indent:48px}
.test-name{left:495px;top:2508px;font-size:14.5px;color:var(--ink)}
.stars{left:495px;top:2544px;display:flex;gap:2px}

/* why choose */
.why-panel{left:0;top:2691px;width:672px;height:454px;border-top-right-radius:36px;background:linear-gradient(120deg,#e9edf1,#d6dce2)}
.why-title{left:104px;top:2796px;font-size:38px;line-height:44px}
.why-text{left:104px;top:2938px;width:260px;font-size:14.5px;line-height:27px;color:var(--muted)}
.why-card{top:2795px;width:249px;height:350px;background:var(--navy);border-top-left-radius:32px;border-top-right-radius:32px;color:#fff;text-align:center}
.why-badge{position:absolute;left:69px;top:30px;width:110px;height:110px;border-radius:50%;border:3px solid #fff;display:flex;align-items:center;justify-content:center}
.why-card h3{position:absolute;left:0;width:100%;top:160px;font-family:"Rajdhani",Arial,sans-serif;font-weight:700;font-size:16px;letter-spacing:.5px}
.why-card p{position:absolute;left:22px;width:205px;top:190px;font-size:13px;line-height:22px;color:#e3e8ee}

/* press */
.press-title{left:0;width:1200px;top:3248px;text-align:center;font-size:38px}
.press-main{left:145px;top:3372px;width:428px;height:366px;background:linear-gradient(135deg,#7d8ea2,#c4ccd4 50%,#5f6f80)}
.press-main .caption{position:absolute;left:75px;top:192px;width:353px;height:174px;background:rgba(28,54,80,.88);color:#fff;padding:20px 24px}
.press-main h4{font-size:18px;font-weight:500;line-height:26px}
.meta{display:flex;align-items:center;gap:8px;font-size:13px;margin:12px 0}
.press-main p{font-size:13px;line-height:21px;color:#dde3e9}
.press-item{left:604px;width:452px;height:172px;border:1px solid var(--line);background:#fff}
.press-item .photo{left:0;top:0;width:190px;height:170px;background:linear-gradient(135deg,#4f7aa2,#a9c1d6 55%,#2f4a66)}
.press-item .body{position:absolute;left:214px;top:18px;width:225px}
.press-item h4{font-size:17px;font-weight:400;color:var(--ink)}
.press-item .meta{color:var(--ink);font-size:13px}
.press-item p{font-size:13px;line-height:21px;color:var(--muted)}

/* contact */
.contact-zone{left:0;top:3863px;width:1200px;height:555px;background:var(--mist)}
.touch-title{left:143px;top:3960px;font-size:36px}
.field{position:absolute;height:40px;border:1px solid var(--line);background:#fff;font-size:13px;color:var(--muted);padding:12px 14px}
.contact-panel{left:740px;top:3863px;width:460px;height:555px;background:var(--navy);border-top-left-radius:110px;border-bottom-left-radius:110px;color:#fff}
.contact-panel .heading{color:#fff}
.c-row{position:absolute;left:53px;display:flex;gap:18px;align-items:flex-start}
.c-icon{width:40px;height:40px;border-radius:50%;background:#fff;display:flex;align-items:center;justify-content:center;flex:none}
.c-label{font-size:16px;line-height:22px}
.c-label b{font-weight:700}
.socials{position:absolute;left:55px;top:437px;display:flex;gap:13px}
.socials span{width:36px;height:36px;border-radius:50%;border:2px solid #fff}

/* footer */
.footer-brand{left:0;width:1200px;top:4486px;display:flex;justify-content:center;align-items:center;gap:24px}
.footer-brand .brand-mark{background:var(--navy)}
.footer-brand .brand-name{color:var(--ink)}
.footer-links{left:0;width:1200px;top:4560px;text-align:center;font-size:15px;color:var(--ink)}
.copyright{left:0;width:1200px;top:4600px;text-align:center;font-size:15px;color:var(--ink)}
</style>
</head>
<body>

<!-- Hero -->
<section class="abs hero">
  <div class="photo" role="img" aria-label="Team of business people working in a bright open office"></div>
  <div class="abs brand"><span class="brand-mark"></span><span class="brand-name">VELUNTA</span></div>
  <nav class="abs nav"><span class="active">HOME</span><span>ABOUT US</span><span>OUR SERVICES</span><span>NEWS</span><span>CONTACT</span></nav>
  <div class="abs lang">EN <svg width="10" height="6" viewBox="0 0 10 6"><path d="M1 1l4 4 4-4" stroke="#fff" fill="none" stroke-width="1.5"/></svg></div>
  <div class="abs slide-arrow" style="left:65px"><svg width="12" height="12" viewBox="0 0 12 12"><path d="M8 1L3 6l5 5" stroke="#1c3650" stroke-width="2" fill="none"/></svg></div>
  <div class="abs slide-arrow" style="left:1104px"><svg width="12" height="12" viewBox="0 0 12 12"><path d="M4 1l5 5-5 5" stroke="#1c3650" stroke-width="2" fill="none"/></svg></div>
  <h1 class="abs hero-title">BUSINESS DEVELOPMENT</h1>
  <p class="abs hero-sub">Nemo enim ipsam voluptatem quia voluptas</p>
  <div class="btn btn-light" style="left:505px;top:493px;width:190px;height:45px">FIND OUT MORE</div>
  <div class="abs dots"><span></span><span></span><span></span></div>
</section>

<!-- Welcome -->
<h2 class="abs heading welcome-title">Welcome to Velunta</h2>
<div class="rule" style="left:143px;top:918px"></div>
<p class="abs welcome-text">Sed ut perspiciatis unde omnis iste natus error sit voluptatem accusantium doloremque laudantium, totam rem aperiam, eaque ipsa quae ab illo inventore veritatis et quasi architecto beatae vitae dicta sunt explicabo. Nemo enim ipsam voluptatem quia voluptas sit aspernatur aut odit aut fugit, sed quia consequuntur magni dolores eos qui ratione voluptatem sequi nesciunt. Neque porro quisquam est, qui dolorem ipsum quia dolor sit amet, consectetur, adipisci velit</p>
<div class="btn btn-dark" style="left:143px;top:1178px;width:130px;height:40px;font-size:15px">READ MORE</div>
<div class="photo welcome-photo" role="img" aria-label="Colleagues meeting around a laptop at a desk"></div>

<!-- Services -->
<div class="abs services-band"></div>
<h2 class="abs heading services-title">OUR SERVICES</h2>
<div class="rule" style="left:568px;top:1508px;background:#fff"></div>

<article class="abs service-card" style="left:0">
  <div class="photo" role="img" aria-label="Businessman in a suit discussing with a colleague" style="background:linear-gradient(135deg,#9aa8b6,#4d5c6c 55%,#2a3644)"></div>
  <div class="shade"></div>
  <div class="service-name" style="top:356px">MARKET RESEARCH</div>
  <p class="service-text" style="top:386px">Sed ut perspiciatis unde omnis iste natus error sit voluptatem accusaum doloremque laudantium</p>
  <svg class="service-go" style="top:458px" width="26" height="14" viewBox="0 0 26 14"><path d="M0 7h24M18 1l6 6-6 6" stroke="#fff" stroke-width="2" fill="none"/></svg>
</article>
<article class="abs service-card" style="left:404px">
  <div class="photo" role="img" aria-label="Two young colleagues reviewing documents together" style="background:linear-gradient(135deg,#c8b5a0,#7a6a5c 55%,#3a3430)"></div>
  <div class="shade" style="background:rgba(20,30,42,.45)"></div>
  <div class="service-icon" style="top:280px"></div>
  <div class="service-name" style="top:290px;left:124px">TAX<br>REPRESENTATION</div>
  <p class="service-text" style="top:364px">Sed ut perspiciatis unde omnis iste natus error sit voluptatem accusaum doloremque laudantium</p>
  <svg class="service-go" style="top:436px" width="26" height="14" viewBox="0 0 26 14"><path d="M0 7h24M18 1l6 6-6 6" stroke="#fff" stroke-width="2" fill="none"/></svg>
</article>
<article class="abs service-card" style="left:808px">
  <div class="photo" role="img" aria-label="Smiling man with a clipboard in a warehouse" style="background:linear-gradient(135deg,#a7ab94,#6f7760 55%,#2f3a42)"></div>
  <div class="shade"></div>
  <div class="service-name" style="top:356px">LOGISTICS</div>
  <p class="service-text" style="top:386px">Sed ut perspiciatis unde omnis iste natus error sit voluptatem accusaum doloremque laudantium</p>
  <svg class="service-go" style="top:458px" width="26" height="14" viewBox="0 0 26 14"><path d="M0 7h24M18 1l6 6-6 6" stroke="#fff" stroke-width="2" fill="none"/></svg>
</article>

<!-- Testimonials -->
<h2 class="abs heading test-title">TESTIMONIALS</h2>
<div class="rule" style="left:563px;top:2280px"></div>
<svg class="abs" style="left:150px;top:2418px" width="20" height="36" viewBox="0 0 20 36"><path d="M17 2L3 18l14 16" stroke="#8a9199" stroke-width="3" fill="none"/></svg>
<svg class="abs" style="left:1026px;top:2418px" width="20" height="36" viewBox="0 0 20 36"><path d="M3 2l14 16L3 34" stroke="#8a9199" stroke-width="3" fill="none"/></svg>
<div class="photo test-photo" role="img" aria-label="Client portrait in an office"></div>
<div class="abs quote-mark" style="left:495px;top:2348px">&ldquo;</div>
<p class="abs test-text">Nemo enim ipsam voluptatem quia voluptas sit aspernatur aut odit aut fugit, sed quia consequuntur magni dolores eos qui ratione uptatem sequi nesciunt. Neque porro quisquam est, qui dolorem ipsum quia dolor sit amet, consectetur, adipisci velit, sed quia non numquam eius modi tempora incidunt</p>
<div class="abs test-name">Jane Roe - Velunta</div>
<div class="abs quote-mark" style="left:742px;top:2500px">&rdquo;</div>
<div class="abs stars">
  <svg width="76" height="14" viewBox="0 0 76 14" fill="#1c3650"><g id="s"><path d="M7 0l2 4.6 5 .5-3.8 3.3 1.1 4.9L7 10.8 2.7 13.3l1.1-4.9L0 5.1l5-.5z"/></g><use href="#s" x="15"/><use href="#s" x="30"/><use href="#s" x="45"/><use href="#s" x="60"/></svg>
</div>

<!-- Why choose -->
<div class="photo why-panel" role="img" aria-label="Faded office background with colleagues at work"></div>
<svg class="abs" style="left:558px;top:2735px" width="26" height="14" viewBox="0 0 26 14"><path d="M26 7H2M8 1L2 7l6 6" stroke="#1c3650" stroke-width="2" fill="none"/></svg>
<svg class="abs" style="left:606px;top:2735px" width="26" height="14" viewBox="0 0 26 14"><path d="M0 7h24M18 1l6 6-6 6" stroke="#1c3650" stroke-width="2" fill="none"/></svg>
<h2 class="abs heading why-title">WHY CHOOSE<br>VELUNTA?</h2>
<p class="abs why-text">Nemo enim ipsam voluptatem quia voluptas sit aspernatur aut odit aut fugit, sed quia consequuntur magni dolores eos qui ratione</p>

<article class="abs why-card" style="left:423px">
  <div class="why-badge"><svg width="54" height="44" viewBox="0 0 54 44" fill="none" stroke="#fff" stroke-width="2"><rect x="6" y="4" width="42" height="28" rx="2"/><path d="M2 38h50M18 14h18M18 20h12"/></svg></div>
  <h3>NEMO ENIM IPSAM</h3>
  <p>Nemo enim ipsam voluptatem quia voluptas sit aspernatur aut odit aut fugit, sed quia conuntur magni dolores eos qui ratione voluptatem sequi nesciunt. Neque porro</p>
</article>
<article class="abs why-card" style="left:679px">
  <div class="why-badge"><svg width="50" height="50" viewBox="0 0 50 50" fill="none" stroke="#fff" stroke-width="2"><circle cx="25" cy="25" r="18"/><path d="M25 13v12l8 6"/></svg></div>
  <h3>NEMO ENIM IPSAM</h3>
  <p>Nemo enim ipsam voluptatem quia voluptas sit aspernatur aut odit aut fugit, sed quia conuntur magni dolores eos qui ratione voluptatem sequi nesciunt. Neque porro</p>
</article>
<article class="abs why-card" style="left:935px">
  <div class="why-badge"><svg width="50" height="46" viewBox="0 0 50 46" fill="none" stroke="#fff" stroke-width="2"><path d="M8 40V26M20 40V16M32 40V22M44 40V8M2 44h46"/></svg></div>
  <h3>NEMO ENIM IPSAM</h3>
  <p>Nemo enim ipsam voluptatem quia voluptas sit aspernatur aut odit aut fugit, sed quia conuntur magni dolores eos qui ratione voluptatem sequi nesciunt. Neque porro</p>
</article>

<!-- Press -->
<h2 class="abs heading press-title">PRESS RELEASES</h2>
<div class="rule" style="left:566px;top:3315px"></div>

<article class="abs press-main">
  <div class="photo" style="inset:0" role="img" aria-label="Group of cheerful colleagues in an office"></div>
  <div class="caption">
    <h4>Nemo enim ipsam voluptatem quia voluptas</h4>
    <div class="meta">
      <svg width="12" height="12" viewBox="0 0 12 12" fill="none" stroke="#fff" stroke-width="1.4"><rect x="1" y="2" width="10" height="9"/><path d="M1 5h10M4 0v3M8 0v3"/></svg>Jan 25, 2020 &nbsp;|&nbsp;
      <svg width="12" height="12" viewBox="0 0 12 12" fill="none" stroke="#fff" stroke-width="1.4"><path d="M1 2h10v6H5l-3 3V8H1z"/></svg>2 comments
    </div>
    <p>Sed ut perspiciatis unde omnis iste natus error sit vuptatem accusantium doloremque</p>
  </div>
</article>

<article class="abs press-item" style="top:3372px">
  <div class="photo" role="img" aria-label="Team collaborating around a desk"></div>
  <div class="body">
    <h4>Nemo enim ipsam volupta</h4>
    <div class="meta">
      <svg width="12" height="12" viewBox="0 0 12 12" fill="none" stroke="#1c3650" stroke-width="1.4"><rect x="1" y="2" width="10" height="9"/><path d="M1 5h10M4 0v3M8 0v3"/></svg>Jan 25, 2020 &nbsp;
      <svg width="12" height="12" viewBox="0 0 12 12" fill="none" stroke="#1c3650" stroke-width="1.4"><path d="M1 2h10v6H5l-3 3V8H1z"/></svg>2 comments
    </div>
    <p>Sed ut perspiciatis unde omnis iste natus error sit vuptatem aum doloremque</p>
  </div>
</article>
<article class="abs press-item" style="top:3565px">
  <div class="photo" role="img" aria-label="Hands working on a laptop with digital charts" style="background:linear-gradient(135deg,#2d4e78,#7fa3c8 55%,#1d3352)"></div>
  <div class="body">
    <h4>Nemo enim ipsam volupta</h4>
    <div class="meta">
      <svg width="12" height="12" viewBox="0 0 12 12" fill="none" stroke="#1c3650" stroke-width="1.4"><rect x="1" y="2" width="10" height="9"/><path d="M1 5h10M4 0v3M8 0v3"/></svg>Jan 25, 2020 &nbsp;
      <svg width="12" height="12" viewBox="0 0 12 12" fill="none" stroke="#1c3650" stroke-width="1.4"><path d="M1 2h10v6H5l-3 3V8H1z"/></svg>2 comments
    </div>
    <p>Sed ut perspiciatis unde omnis iste natus error sit vuptatem aum doloremque</p>
  </div>
</article>

<!-- Contact -->
<div class="abs contact-zone"></div>
<h2 class="abs heading touch-title">GET IN TOUCH</h2>
<div class="rule" style="left:143px;top:4020px"></div>
<div class="field" style="left:143px;top:4055px;width:251px;font-size:11px">First Name</div>
<div class="field" style="left:407px;top:4055px;width:251px">Last Name</div>
<div class="field" style="left:143px;top:4108px;width:515px">Email Address</div>
<div class="field" style="left:143px;top:4162px;width:251px">City</div>
<div class="field" style="left:407px;top:4162px;width:251px">Phone Number</div>
<div class="field" style="left:143px;top:4216px;width:515px;height:54px">Message</div>
<div class="btn btn-dark" style="left:143px;top:4290px;width:163px;height:42px;font-size:17px">SUBMIT NOW</div>

<aside class="abs contact-panel">
  <h2 class="abs heading" style="left:53px;top:100px;font-size:32px">CONTACT US</h2>
  <div class="rule" style="left:53px;top:157px;background:#fff;width:56px"></div>
  <div class="c-row" style="top:195px">
    <span class="c-icon"><svg width="14" height="18" viewBox="0 0 14 18"><path d="M7 0a7 7 0 017 7c0 5-7 11-7 11S0 12 0 7a7 7 0 017-7z" fill="#1c3650"/><circle cx="7" cy="7" r="2.5" fill="#fff"/></svg></span>
    <div class="c-label" style="font-size:15px">Address:<br><b>12, Harbour Lane<br>LKR 2040 Lakeside</b></div>
  </div>
  <div class="c-row" style="top:288px">
    <span class="c-icon"><svg width="16" height="16" viewBox="0 0 16 16"><path d="M3 1l3 3-1.5 2.5a10 10 0 005 5L12 10l3 3-2 2C6 15 1 10 1 3z" fill="#1c3650"/></svg></span>
    <div class="c-label" style="font-size:18px">Phone:<br><b>+808 4410 2297</b></div>
  </div>
  <div class="c-row" style="top:363px">
    <span class="c-icon"><svg width="18" height="13" viewBox="0 0 18 13"><rect width="18" height="13" rx="1.5" fill="#1c3650"/><path d="M1 1l8 6 8-6" stroke="#fff" stroke-width="1.4" fill="none"/></svg></span>
    <div class="c-label" style="font-size:15px">Email:<br><b>info@velunta.com</b></div>
  </div>
  <div class="socials"><span></span><span></span><span></span><span></span></div>
</aside>

<!-- Footer -->
<footer>
  <div class="abs footer-brand"><span class="brand-mark"></span><span class="brand-name">VELUNTA</span></div>
  <div class="abs footer-links">Home &nbsp;|&nbsp; About Us &nbsp;|&nbsp; Our Services &nbsp;|&nbsp; News &nbsp;|&nbsp; Contact</div>
  <div class="abs copyright">Copyright 2020 Velunta. All rights reserved.</div>
</footer>

</body>
</html>
```